Martial Art workout site needs web page design

We need a web page designed for our new martial art web site that presents innovated, monthly workouts, done by beautiful models
Web page should include
- a home page
- Page for the monthly workout
- Gallery page for the models (pics & video)
-Archived page for past workout
- Page to sign up for monthly updates
- Sponsor Page

Industry/Entity Type

Martial Art

```html
<!DOCTYPE html>
<html lang="en">
<head>
<meta charset="utf-8">
<title>Ridge Vale Martial Arts</title>
<link href="https://fonts.googleapis.com/css2?family=Source+Sans+3:ital,wght@0,300;0,400;0,600;1,300&family=Oswald:wght@400;500&display=swap" rel="stylesheet">
<style>
:root{
  --orange:#f57c00;
  --orange-light:#ff9a1f;
  --dark:#1c1c1c;
  --dark-2:#333;
  --text:#555;
  --text-soft:#777;
  --navy:#1c2a7a;
  --white:#fff;
  --line:#e4e4e4;
}
*{margin:0;padding:0;box-sizing:border-box}
html,body{width:1022px;height:1200px;overflow:hidden}
body{position:relative;background:var(--white);font-family:"Source Sans 3",sans-serif;color:var(--text)}
.header-band{position:absolute;left:0;top:0;width:1022px;height:248px;background:linear-gradient(#2a2a2a,#0e0e0e)}
.brand{position:absolute;left:94px;top:28px}
.brand-name{font-size:42px;font-weight:600;color:var(--orange);line-height:1;letter-spacing:-.5px}
.brand-sub{font-size:15px;font-weight:600;color:var(--white);margin-left:96px;margin-top:2px}
.join{position:absolute;right:96px;top:44px;text-align:right}
.join-label{color:var(--white);font-size:14px}
.join-phone{color:var(--orange-light);font-size:22px;line-height:1}
.page{position:absolute;left:90px;top:101px;width:839px;height:985px;background:var(--white);box-shadow:0 0 10px rgba(0,0,0,.12)}
.nav{display:flex;height:43px;background:linear-gradient(var(--orange-light),var(--orange));border-radius:3px 3px 0 0}
.nav a{color:var(--white);text-decoration:none;font-family:"Oswald",sans-serif;font-weight:400;font-size:13.5px;display:flex;align-items:center;justify-content:center;border-right:1px solid rgba(255,255,255,.35)}
.nav a:last-child{border-right:0}
.hero{position:relative;height:357px;background:linear-gradient(100deg,#cdbb98 0%,#e9dfc8 45%,#d8cdb4 65%,#6d5a44 100%)}
.hero-caption{position:absolute;left:536px;top:167px;width:271px;height:129px;background:rgba(255,255,255,.72);padding:16px 26px}
.hero-caption h2{font-family:"Oswald",sans-serif;font-weight:500;font-size:22px;line-height:1.15;color:var(--orange)}
.hero-caption h2 span{display:block;color:#333;font-size:26px}
.hero-caption p{font-size:11.5px;color:#777;margin-top:6px;line-height:1.4}
.dots{position:absolute;left:388px;top:334px;display:flex;gap:3px}
.dots i{width:11px;height:11px;border-radius:50%;background:var(--white)}
.welcome{position:absolute;left:26px;top:427px;width:500px}
.welcome h1{font-size:23px;font-weight:400;color:var(--orange)}
.welcome .lead{font-size:15px;line-height:1.3;color:#666;margin-top:8px;font-weight:300}
.welcome p.body{font-size:11px;line-height:1.75;color:var(--text-soft);margin-top:8px;font-weight:300}
.video-title{position:absolute;left:548px;top:427px;font-size:22px;font-weight:300;color:#222}
.video{position:absolute;left:550px;top:461px;width:274px;height:185px;background:linear-gradient(#7b8f5c,#5f8d3a)}
.play{position:absolute;left:120px;top:70px}
.signup{position:absolute;left:550px;top:658px;width:274px;height:57px;background:linear-gradient(var(--orange-light),var(--orange));border-radius:2px;color:var(--white);display:flex;align-items:center;padding-left:18px;gap:14px}
.signup small{display:block;font-family:"Oswald",sans-serif;font-weight:400;font-size:13px;opacity:.9}
.signup strong{display:block;font-family:"Oswald",sans-serif;font-weight:500;font-size:15.5px;line-height:1}
.testimonial{position:absolute;left:552px;top:729px;width:270px;height:181px;border:1px solid var(--line);background:linear-gradient(#fff,#f2f2f2);padding:18px 20px}
.testimonial h3{font-size:19px;font-weight:400;color:#222}
.testimonial blockquote{font-style:italic;font-weight:300;font-size:11px;line-height:1.6;color:#666;margin-top:6px;padding-left:10px}
.testimonial cite{display:block;font-style:normal;font-size:12px;color:#555;margin-top:4px;padding-left:10px}
.section-title{font-family:"Oswald",sans-serif;font-weight:400;font-size:17px}
.gallery{position:absolute;left:28px;top:673px}
.gallery .section-title{color:var(--navy)}
.thumbs{display:grid;grid-template-columns:repeat(3,78px);gap:9px;margin-top:10px}
.thumbs div{height:65px;border:1px solid #ddd;box-shadow:0 1px 2px rgba(0,0,0,.15)}
.why{position:absolute;left:312px;top:673px;width:200px}
.why .section-title{color:var(--orange)}
.why p{font-size:10.5px;line-height:1.68;color:var(--text-soft);margin-top:6px;font-weight:300}
.why ul{list-style:none;margin-top:10px}
.why li{font-size:10.5px;color:#333;border-bottom:1px solid #eee;padding:5px 0 6px 14px;position:relative}
.why li::before{content:"";position:absolute;left:4px;top:10px;border-left:4px solid #444;border-top:3px solid transparent;border-bottom:3px solid transparent}
.footer{position:absolute;left:0;top:1090px;width:1022px;height:110px;background:linear-gradient(#3a3a3a,#1a1a1a);border-top:3px solid #555}
.footer-links{position:absolute;left:112px;top:24px;font-size:11.5px;color:var(--white)}
.footer-links a{color:var(--white);text-decoration:none}
.footer-links span{margin:0 5px}
.copyright{position:absolute;left:112px;top:50px;font-size:9px;color:#ccc}
.social{position:absolute;left:816px;top:27px;display:flex;gap:4px}
.social i{width:22px;height:22px;border-radius:50%;background:var(--white)}
</style>
</head>
<body>
<div class="header-band"></div>
<div class="brand">
  <div class="brand-name">Ridge Vale</div>
  <div class="brand-sub">Martial Arts</div>
</div>
<div class="join">
  <div class="join-label">JOIN US NOW</div>
  <div class="join-phone">555.204.7781</div>
</div>

<div class="page">
  <nav class="nav">
    <a style="width:100px">HOME</a>
    <a style="width:108px">ABOUT US</a>
    <a style="width:170px">MONTHLY WORKOUT</a>
    <a style="width:104px">GALLERY</a>
    <a style="width:106px">ARCHIVES</a>
    <a style="width:116px">SPONSORS</a>
    <a style="flex:1">CONTACT US</a>
  </nav>
  <div class="hero" role="img" aria-label="Two karate practitioners in white uniforms kicking on a rocky seashore at sunset">
    <div class="hero-caption">
      <h2>WE GIVE TRAINING<span>FOR MARTIAL ARTS</span></h2>
      <p>Phasellus felis dolor, scelerisque a, tempus eget, lobortis id, libero.</p>
    </div>
    <div class="dots"><i></i><i></i><i></i><i></i><i></i></div>
  </div>

  <section class="welcome">
    <h1>Welcome to Ridge Vale Mainpage..</h1>
    <p class="lead">Phasellus felis dolor scelerisque a tempus eget lobortis id libero Donec scelerisque leo ac risus Praesent sit amet est</p>
    <p class="body">Nulla elementum dui ut augue. Aliquam vehicula mi at mauris. Maecenas placerat, nisl at consequat rhoncus, sem nunc gravida justo, quis eleifend arcu velit quis lacus. Morbi magna magna, tincidunt a, mattis non, imperdiet vitae, tellus. Sed odio est, auctor ac, sollicitudin in, consequat vitae, orci. Fusce id felis. Vivamus sollicitudin metus eget eros.</p>
    <p class="body">Mauris vel lacus vitae felis vestibulum volutpat. Etiam est nunc, venenatis in, tristique eu, imperdiet ac, nisl. Cum sociis natoque penatibus et magnis dis parturient montes, nascetur ridiculus mus.</p>
  </section>

  <h2 class="video-title">Watch Our Video</h2>
  <div class="video" role="img" aria-label="Video still of two karate students sparring on a park lawn with spectators">
    <svg class="play" width="34" height="34" viewBox="0 0 34 34"><circle cx="17" cy="17" r="15.5" fill="#222" stroke="#fff" stroke-width="2.5"/><path d="M13 10l11 7-11 7z" fill="#fff"/></svg>
  </div>
  <div class="signup">
    <svg width="30" height="26" viewBox="0 0 30 26"><rect x="1" y="1" width="28" height="24" rx="3" fill="#fff"/><path d="M2 5l13 9 13-9" fill="none" stroke="#f57c00" stroke-width="2.5"/></svg>
    <div><small>SIGN UP FOR</small><strong>MONTHLY UPDATES</strong></div>
  </div>
  <aside class="testimonial">
    <h3>What Our Students Say</h3>
    <blockquote>Curabitur iaculis tempus eros. Curabitur vel mi sit amet magna malesuada ultrices. Ut nisi erat, fermentum vel, congue id, euismod in, elit. Fusce ultricies, orci ac feugiat suscipit, leo massa sodales velit, et scelerisque mi tortor at ipsum.</blockquote>
    <cite>By Author Name</cite>
  </aside>

  <section class="gallery">
    <h2 class="section-title">PHOTO GALLERY</h2>
    <div class="thumbs">
      <div role="img" aria-label="Karate class in a bright dojo" style="background:#d9dde0"></div>
      <div role="img" aria-label="Two fighters sparring" style="background:#a08a6e"></div>
      <div role="img" aria-label="Jumping kick against blue sky" style="background:#4f86c6"></div>
      <div role="img" aria-label="Student kicking a pad" style="background:#c9ced4"></div>
      <div role="img" aria-label="Young student portrait" style="background:#e8ddd2"></div>
      <div role="img" aria-label="Fighter in red gloves" style="background:#4a2222"></div>
      <div role="img" aria-label="Martial artist kicking toward camera" style="background:#5fae48"></div>
      <div role="img" aria-label="Children in karate uniforms" style="background:#e3dcd3"></div>
      <div role="img" aria-label="Group jumping in silhouette" style="background:#9bb3c8"></div>
    </div>
  </section>

  <section class="why">
    <h2 class="section-title">WHY JOIN US</h2>
    <p>Mauris vel lacus vitae felis vestibulum volutpat. Etiam est nunc, venenatis in, tristique eu, imperdiet ac, nisl. Cum sociis natoque penatibus et magnis dis</p>
    <ul>
      <li>Mauris vel lacus vitae</li>
      <li>Felis vestibulum volutpat</li>
      <li>Etiam est nunc venenatis in</li>
      <li>Tristique eu imperdiet ac nisl.</li>
      <li>Cum sociis natoque penatibus et</li>
    </ul>
  </section>
</div>

<footer class="footer">
  <div class="footer-links">
    <a>Home</a><span>|</span><a>Services We Provide</a><span>|</span><a>Patient Form</a><span>|</span><a>Instant Appointment</a><span>|</span><a>Insurances Accepted</a><span>|</span><a>Patient Testimonials</a><span>|</span><a>About Us</a><span>|</span><a>Contact</a>
  </div>
  <div class="copyright">© 2012 Company Name.&nbsp; All right reserved.&nbsp; Term of Use</div>
  <div class="social"><i></i><i></i><i></i><i></i></div>
</footer>
</body>
</html>
```